NWSU, Bureau of Digital Services responsive website

We need a responsive web design for NWSU's Bureau of Digital Services, see https://bds.nwsu-example.edu/ that will look good on all three platforms, PC Web browser, tablet & phone. Please use http://www.nwsu-example.edu as and indication of design genre. A full design will show off all three versions of what the wide screen, tablet and phone will look like,using good responsive design concepts. Minimal text embedded in images for good accessibility. An acceptable design must meet WCAG 2.0 standards for color contrast and beyond. Please note, that much more work could come to good designers, if this works out!
KEY concepts: Cultured, Visionary, Perseverance, catalytic
For the 4 pages, I want to see the home page, the tablet view, the mobile view and also a sub theme page

Target Market(s)

Faculty, Staff, Students, Technologists

Industry/Entity Type

Information Technology

Coding

Coded - Design and coding required

Number of Pages Required

4 page

Font styles to use
Serif
Sans Serif
Other font styles liked:
• Karbon

Colors
0492cd
3176b5
fbed22
ffc214
fbee3e

Requirements
Must have
• My project must use the existing BDS logo on the current website: http://bds.nwsu-example.edu, it must look good with responsive design, thus in all sizes, for a PC, on a tablet on and a mobile phone.
• It must have a way to feature events and content, it must feature the current homepage content, but have a new navigation plan that works well with responsive design. An acceptable design must meet WCAG 2.0 standards for color contrast and beyond. It must have a menu that reduces down to an icon on a mobile phone, it must not find a way to get content to stack vertically
Nice to have
• It would be nice to see their be continuity between the PC, TAblet and mobile phone design, it would be nice to see elements of http://www.nwsu-example.edu embedded into the design
Should not have
• text embedded in the logo, a design that is not conducive to responsive design, it must not use ANY tables

```html
<!DOCTYPE html>
<html lang="en">
<head>
<meta charset="utf-8">
<title>Bureau of Digital Services NWSU</title>
<link href="https://fonts.googleapis.com/css2?family=Lato:wght@400;700&family=Oswald:wght@400&family=Tinos:wght@400;700&display=swap" rel="stylesheet">
<style>
:root{
  --blue:#0492cd;
  --blue-deep:#3176b5;
  --yellow:#ffc214;
  --yellow-lite:#fbed22;
  --ink:#222;
  --text:#333;
  --grey-bg:#f4f4f2;
  --footer:#333;
  --footer-deep:#1f1f1f;
  --white:#fff;
}
*{box-sizing:border-box;margin:0;padding:0}
html,body{width:717px;height:1200px;overflow:hidden}
body{font-family:'Lato',sans-serif;color:var(--text);background:var(--white);position:relative}
.abs{position:absolute}

/* header */
.topline{left:0;top:0;width:717px;height:3px;display:flex}
.topline span{flex:1}
.header{left:0;top:3px;width:717px;height:60px;background:var(--white)}
.brand{left:78px;top:14px;display:flex;align-items:center;gap:8px}
.brand-dot{width:26px;height:26px;border-radius:50%;background:var(--blue-deep)}
.brand-name{font-family:'Lato',sans-serif;font-weight:700;font-size:15px;color:var(--ink);letter-spacing:.3px}
.contact-line{left:425px;top:8px;display:flex;gap:14px;align-items:center;font-size:11.5px;color:var(--blue-deep)}
.contact-line .phone{font-size:12.5px}
.contact-line .mail{font-size:9.5px;font-weight:700}
.contact-line svg{vertical-align:-2px;margin-right:4px}
.search{left:497px;top:30px;width:141px;height:19px;border:1px solid #ccc;border-radius:10px;font-size:8px;color:#777;padding:4px 9px}
.search svg{position:absolute;right:7px;top:4px}

/* nav */
.nav{left:0;top:63px;width:717px;height:28px;background:var(--blue)}
.nav ul{list-style:none;display:flex;position:absolute;left:78px;top:0;height:28px}
.nav li{height:28px;line-height:28px;font-size:9.5px;color:var(--white);text-align:center;border-right:1px solid rgba(255,255,255,.35)}
.nav li.active{background:var(--yellow);color:var(--ink)}
.nav li:last-child{border-right:none}

/* hero */
.hero{left:0;top:91px;width:717px;height:253px;background:linear-gradient(100deg,#5b8fd8 0%,#a9c8f0 35%,#6f9de0 60%,#2d5fae 100%)}
.hero-caption{left:70px;top:35px;width:230px;text-align:center;font-family:'Tinos',serif;font-size:20.5px;line-height:26.5px;color:var(--white)}
.hero-caption b{font-weight:700}
.hero-arrow{top:105px;width:36px;height:36px;border-radius:50%;background:rgba(40,60,100,.55);border:2px solid rgba(255,255,255,.5)}
.hero-arrow svg{position:absolute;left:10px;top:9px}

/* services */
.services{left:0;top:344px;width:717px;height:178px;background:linear-gradient(90deg,#3b3e44,#6c7078 45%,#4a4d53 70%,#2f3136);border-top:2px solid #888}
.service{top:19px;width:101px;text-align:center}
.service-box{width:101px;height:106px;background:rgba(150,150,150,.55);border-radius:3px;position:relative}
.service-icon{position:absolute;left:23px;top:25px;width:54px;height:54px;border-radius:50%;background:var(--yellow);border:2px solid var(--white);display:flex;align-items:center;justify-content:center}
.service-label{margin-top:9px;margin-left:-20px;width:141px;font-size:10.5px;line-height:15px;font-weight:700;color:var(--white);text-transform:uppercase}

/* welcome */
.welcome{left:0;top:522px;width:717px;height:221px;background:var(--grey-bg);text-align:center}
.welcome h1{position:absolute;left:0;top:10px;width:717px;font-family:'Oswald',sans-serif;font-weight:400;font-size:17px;color:var(--ink)}
.welcome h1 span{color:var(--blue-deep);margin-left:4px}
.divider{position:absolute;left:152px;top:44px;width:414px;height:1px;background:#ccc}
.dots{position:absolute;left:340px;top:40px;display:flex;gap:4px}
.dots i{width:9px;height:9px;border-radius:50%;border:1px solid #bbb;background:var(--white)}
.dots i.on{background:var(--blue);border-color:var(--blue)}
.lead{position:absolute;left:88px;top:58px;width:541px;font-size:9.3px;line-height:16px;font-weight:700;color:var(--ink)}
.body-copy{position:absolute;left:88px;top:101px;width:541px;font-size:7.5px;line-height:14.5px}
.btn{position:absolute;left:327px;top:173px;width:62px;height:20px;background:var(--blue);color:var(--white);font-family:'Oswald',sans-serif;font-size:8.5px;line-height:20px;border-radius:2px}

/* news + initiatives */
.news{left:0;top:743px;width:358px;height:257px;background:var(--blue-deep)}
.news h2{position:absolute;left:82px;top:10px;font-size:12.5px;font-weight:700;color:var(--white)}
.news .rule{position:absolute;left:82px;top:34px;width:262px;height:1px;background:rgba(255,255,255,.5)}
.news .rule::before{content:"";position:absolute;left:0;top:-1px;width:134px;height:2px;background:var(--white)}
.news-item{left:82px;width:270px;display:flex;gap:9px}
.news-thumb{width:80px;height:63px;border:3px solid var(--white);flex:none}
.news-item h3{font-size:10px;font-weight:400;color:var(--white);margin-top:2px;white-space:nowrap}
.news-item p{font-size:7.5px;line-height:14px;color:var(--white);margin-top:2px}

.initiatives{left:358px;top:743px;width:359px;height:257px;background:linear-gradient(90deg,#0a86c7,#1aa2dc 70%,#0b8fcf)}
.initiative{left:22px;width:330px;display:flex;gap:12px}
.init-icon{width:37px;height:37px;border-radius:50%;background:var(--white);border:2px solid #cde;flex:none;display:flex;align-items:center;justify-content:center}
.initiative h3{font-size:12.5px;font-weight:400;color:var(--white);line-height:15px}
.initiative p{font-size:7.3px;line-height:10.5px;color:var(--white)}

/* contact */
.touch{left:0;top:1000px;width:717px;height:143px;background:var(--white)}
.touch h2{position:absolute;left:0;top:14px;width:717px;text-align:center;font-size:13.5px;font-weight:700;color:var(--ink)}
.touch h2 span{color:var(--blue-deep);font-weight:400}
.touch h2 svg{vertical-align:-1px;margin-right:6px}
.touch .dotted{position:absolute;left:226px;top:35px;width:265px;border-top:1px dotted #999}
.touch .sub{position:absolute;left:0;top:42px;width:717px;text-align:center;font-size:8px}
.field{height:18px;border:1px solid #ccc;border-radius:3px;font-size:7px;color:#444;padding:4px 7px}
.field.select{background:linear-gradient(90deg,#fff 85%,#e8e8e8 85%)}
.field.select svg{position:absolute;right:5px;top:6px}
.submit{left:334px;top:112px;width:49px;height:17px;background:var(--blue);color:var(--white);font-size:8px;font-weight:700;text-align:center;line-height:17px;border-radius:2px}

/* footer */
.footer-nav{left:0;top:1143px;width:717px;height:29px;background:var(--footer);display:flex;justify-content:center;align-items:center;font-size:8.5px;color:var(--white)}
.footer-nav span{padding:0 12px}
.footer-nav i{font-style:normal;color:#bbb}
.footer-bar{left:0;top:1172px;width:717px;height:28px;background:var(--footer-deep);border-top:1px solid #444}
.copyright{left:80px;top:9px;font-size:8px;color:var(--white)}
.social{left:511px;top:5px;display:flex;gap:4px}
.social i{width:18px;height:18px;display:block}
</style>
</head>
<body>

<div class="abs topline"><span style="background:var(--blue)"></span><span style="background:var(--yellow-lite)"></span><span style="background:var(--blue)"></span><span style="background:var(--yellow-lite)"></span></div>

<header class="abs header">
  <div class="abs brand"><span class="brand-dot"></span><span class="brand-name">BDS · Bureau of Digital Services NWSU</span></div>
  <div class="abs contact-line">
    <span class="phone"><svg width="8" height="11" viewBox="0 0 8 11"><path d="M2 0h2l1 3-1.5 1c.5 1.5 1.2 2.5 2.3 3.3L7 6l1 2.3-1 1.7C3.5 10 0 5 1 1z" fill="#3176b5"/></svg>(555) 014-2290</span>
    <span class="mail"><svg width="13" height="9" viewBox="0 0 13 9"><rect width="13" height="9" fill="#3176b5"/><path d="M0 0l6.5 5L13 0" stroke="#fff" fill="none"/></svg>frontdesk@bds.nwsu-example.edu</span>
  </div>
  <div class="abs search">Search<svg width="10" height="10" viewBox="0 0 10 10"><circle cx="4" cy="4" r="3" stroke="#999" stroke-width="1.4" fill="none"/><path d="M6.3 6.3L9.5 9.5" stroke="#999" stroke-width="1.5"/></svg></div>
</header>

<nav class="abs nav">
  <ul>
    <li class="active" style="width:72px">HOME</li>
    <li style="width:66px">ABOUT</li>
    <li style="width:79px">CONTACT</li>
    <li style="width:118px">STAFF DIRECTORY</li>
    <li style="width:99px">OUR EXPERTS</li>
    <li style="width:60px">NEWS</li>
    <li style="width:61px">EVENTS</li>
  </ul>
</nav>

<section class="abs hero" role="img" aria-label="Photo of a team meeting in silhouette around a conference table against a blue globe backdrop">
  <p class="abs hero-caption">The <b>Mobile Web Framewor</b>k Facilitates The Development of A Robust, Feature-rich, Cross-platform Mobile Web Presence.</p>
  <span class="abs hero-arrow" style="left:27px"><svg width="12" height="16" viewBox="0 0 12 16"><path d="M10 1L3 8l7 7" stroke="#fff" stroke-width="2" fill="none"/></svg></span>
  <span class="abs hero-arrow" style="left:650px"><svg width="12" height="16" viewBox="0 0 12 16"><path d="M2 1l7 7-7 7" stroke="#fff" stroke-width="2" fill="none"/></svg></span>
</section>

<section class="abs services" role="img" aria-label="Dim background photo of hands at a laptop with floating screens">
  <div class="abs service" style="left:101px"><div class="service-box"><span class="service-icon"><svg width="26" height="22" viewBox="0 0 26 22"><rect x="9" y="0" width="8" height="6" fill="#222"/><rect x="0" y="15" width="7" height="6" fill="#222"/><rect x="9.5" y="15" width="7" height="6" fill="#222"/><rect x="19" y="15" width="7" height="6" fill="#222"/><path d="M13 6v4M3.5 15v-5h19v5M13 10v5" stroke="#222" stroke-width="1.6" fill="none"/></svg></span></div><p class="service-label">Organizational Structure</p></div>
  <div class="abs service" style="left:239px"><div class="service-box"><span class="service-icon"><svg width="26" height="26" viewBox="0 0 26 26"><path d="M4 22L18 8M8 4l6 6 3-3-6-6z" stroke="#222" stroke-width="3" fill="#222"/><path d="M22 22L9 9M4 5a3 3 0 1 0 4-1" stroke="#222" stroke-width="3" fill="none"/></svg></span></div><p class="service-label">Software &amp;<br>Services</p></div>
  <div class="abs service" style="left:377px"><div class="service-box"><span class="service-icon"><svg width="22" height="26" viewBox="0 0 22 26"><rect x="8" y="1" width="6" height="12" rx="1" fill="#222"/><path d="M6 11a8 8 0 0 0 8 11" stroke="#222" stroke-width="2.5" fill="none"/><rect x="2" y="22" width="18" height="3" fill="#222"/><rect x="7" y="13" width="8" height="3" fill="#222"/></svg></span></div><p class="service-label">Research &amp;<br>Learning</p></div>
  <div class="abs service" style="left:514px"><div class="service-box"><span class="service-icon"><svg width="28" height="22" viewBox="0 0 28 22"><circle cx="5" cy="5" r="3" fill="#222"/><circle cx="14" cy="4" r="3" fill="#222"/><circle cx="23" cy="5" r="3" fill="#222"/><rect x="1" y="9" width="8" height="12" rx="2" fill="#222"/><rect x="10" y="8" width="8" height="13" rx="2" fill="#222"/><rect x="19" y="9" width="8" height="12" rx="2" fill="#222"/></svg></span></div><p class="service-label">Community &amp;<br>Governance</p></div>
</section>

<section class="abs welcome">
  <h1>WELCOME TO<span>BUREAU OF DIGITAL SERVICES NWSU</span></h1>
  <div class="divider"></div>
  <div class="dots"><i></i><i class="on"></i><i></i></div>
  <p class="lead">Lorem ipsum dolor sit amet, consectetur adipiscing elit. Duis ac blandit nis Maecenas ac pharetra elit, et pharetra diam. Curabitur ex risuslacinia sit amet libero. Uteu enim turpis. Nunc nulla orci, dictum vel rhoncus sit a accumsan vitae felis.&nbsp; Aenean sit amet sem a lorem</p>
  <p class="body-copy">Lorem ipsum dolor sit amet, consectetur adipiscing elit. Duis ac blandit nis Maecenas ac pharetra elit, et pharetra diam. Curabitur ex risus, viverra ut laoreet quis, lacinia sit amet libero.&nbsp; Uteu enim turpis. Nunc nulla orci, dictum vel rhoncus sit a accumsan vitae felis. Aenean sit amet sem a lorem posuere tempor. Phasellus rat o&nbsp; elementum ac dictum et,&nbsp; scelerisque ac nisi. Nullam euismod non nunc lacinia aliquam. Quisque accumsan pharetra massa, eu sodales nunc posuere viverra.</p>
  <span class="btn">READ MORE</span>
</section>

<section class="abs news">
  <h2>News &amp; Announcements</h2>
  <div class="rule"></div>
  <article class="abs news-item" style="top:46px"><div class="news-thumb" role="img" aria-label="Aerial site plan photo" style="background:linear-gradient(135deg,#9a9a86,#c9c4b0)"></div><div><h3>Lorem ipsum dolor sit amet, consectetur</h3><p>Lorem ipsum dolor sit amet, consectetuer adipiscing elit, sed diam nonummy nibh euismod tincidunt ut laoreet dolore</p></div></article>
  <article class="abs news-item" style="top:117px"><div class="news-thumb" role="img" aria-label="Terms and conditions notice graphic" style="background:linear-gradient(180deg,#e7eef8,#2a5ea8 55%,#e8eef6)"></div><div><h3>Lorem ipsum dolor sit amet, consectetur</h3><p>Lorem ipsum dolor sit amet, consectetuer adipiscing elit, sed diam nonummy nibh euismod tincidunt ut laoreet dolore</p></div></article>
  <article class="abs news-item" style="top:187px"><div class="news-thumb" role="img" aria-label="Photo of banknotes" style="background:linear-gradient(135deg,#c8a888,#8fa3a0)"></div><div><h3>Lorem ipsum dolor sit amet, consectetur</h3><p>Lorem ipsum dolor sit amet, consectetuer adipiscing elit, sed diam nonummy nibh euismod tincidunt ut laoreet dolore</p></div></article>
</section>

<section class="abs initiatives">
  <div class="abs initiative" style="top:11px"><span class="init-icon"><svg width="18" height="20" viewBox="0 0 18 20"><circle cx="9" cy="8" r="5" stroke="#222" stroke-width="1.5" fill="none"/><rect x="6.5" y="13" width="5" height="4" fill="#222"/><path d="M9 0v1.5M1 8h1.5M15.5 8H17M3 2l1 1M15 2l-1 1" stroke="#222" stroke-width="1.3"/></svg></span><div><h3>Initiatives</h3><p>Lorem ipsum dolor sit amet, consectetuer adipiscing elit, sed diam nonummy nibh euismod tincidunt ut laoreet dolore</p></div></div>
  <div class="abs initiative" style="top:60px"><span class="init-icon"><svg width="20" height="20" viewBox="0 0 20 20"><circle cx="10" cy="10" r="7" stroke="#222" stroke-width="1.5" fill="none"/><ellipse cx="10" cy="10" rx="3" ry="7" stroke="#222" stroke-width="1.2" fill="none"/><path d="M3 10h14" stroke="#222" stroke-width="1.2"/><path d="M1 6a10 10 0 0 1 16-4" stroke="#222" stroke-width="1.5" fill="none"/></svg></span><div><h3>Strategy, Governance &amp; Policy</h3><p>Lorem ipsum dolor sit amet, consectetuer adipiscing elit, sed diam nonummy nibh euismod tincidunt ut laoreet dolore</p></div></div>
  <div class="abs initiative" style="top:109px"><span class="init-icon"><svg width="20" height="20" viewBox="0 0 20 20"><circle cx="5" cy="4" r="2.5" fill="#222"/><circle cx="15" cy="4" r="2.5" fill="#222"/><rect x="2" y="7" width="6" height="7" rx="1.5" fill="#222"/><rect x="12" y="7" width="6" height="7" rx="1.5" fill="#222"/><rect x="7" y="12" width="6" height="2" fill="#222"/><rect x="3" y="15" width="3" height="4" fill="#222"/><rect x="14" y="15" width="3" height="4" fill="#222"/></svg></span><div><h3>Resources &amp; Services</h3><p>Lorem ipsum dolor sit amet, consectetuer adipiscing elit, sed diam nonummy nibh euismod tincidunt ut laoreet dolore</p></div></div>
  <div class="abs initiative" style="top:157px"><span class="init-icon"><svg width="22" height="22" viewBox="0 0 22 22"><circle cx="11" cy="11" r="9.5" fill="#222"/><path d="M6 11l3.5 3.5L16 8" stroke="#fff" stroke-width="2.4" fill="none"/></svg></span><div><h3>Industry Partnerships</h3><p>Lorem ipsum dolor sit amet, consectetuer adipiscing elit, sed diam nonummy nibh euismod tincidunt ut laoreet dolore</p></div></div>
  <div class="abs initiative" style="top:207px"><span class="init-icon"><svg width="20" height="20" viewBox="0 0 20 20"><circle cx="10" cy="8" r="6" fill="#222"/><path d="M4 15a8 8 0 0 0 12 0M10 16v3M6 19h8" stroke="#222" stroke-width="1.6" fill="none"/></svg></span><div><h3>Outreach &amp; Learning</h3><p>Lorem ipsum dolor sit amet, consectetuer adipiscing elit, sed diam nonummy nibh euismod tincidunt ut laoreet dolore</p></div></div>
</section>

<section class="abs touch">
  <h2><svg width="14" height="10" viewBox="0 0 14 10"><rect width="14" height="10" fill="#3176b5"/><path d="M0 0l7 5.5L14 0" stroke="#fff" fill="none"/></svg>Get In <span>Touch With Us</span></h2>
  <div class="dotted"></div>
  <p class="sub">Lorem ipsum dolor sit amet, consectetur adipiscing elit. Duis ac blandit nis Maecenas ac pharetra elit</p>
  <div class="abs field" style="left:93px;top:64px;width:124px">Name</div>
  <div class="abs field" style="left:230px;top:64px;width:124px">Email</div>
  <div class="abs field" style="left:93px;top:87px;width:124px">Phone Number</div>
  <div class="abs field select" style="left:230px;top:87px;width:124px">Product Features<svg width="8" height="5" viewBox="0 0 8 5"><path d="M0 0l4 5 4-5z" fill="#666"/></svg></div>
  <div class="abs field" style="left:364px;top:64px;width:262px;height:41px">Your Message</div>
  <span class="abs submit">SUBMIT</span>
</section>

<footer>
  <div class="abs footer-nav"><span>Home</span><i>|</i><span>About</span><i>|</i><span>Contact</span><i>|</i><span>Staff Directory</span><i>|</i><span>Our Experts</span><i>|</i><span>News</span><i>|</i><span>Events</span></div>
  <div class="abs footer-bar">
    <p class="abs copyright">© 2015 BDS. All Rights Reserved.</p>
    <div class="abs social"><i style="background:#3b5998"></i><i style="background:#1da1f2"></i><i style="background:#2b5fa8"></i><i style="background:#d62020"></i><i style="background:#2f8ee0"></i><i style="background:#3b7fc4"></i></div>
  </div>
</footer>

</body>
</html>
```